Passport Brochure

We are a start-up training and staffing company called Verlow Consulting. We assist people in getting work in the Financial Industry.
We need a brochure for our new "Career Beacon Program".
We've put together a mock up of what we are looking for but we need someone to put a more professional touch on it, see "Creative Brief" attached obviously the pictures are just examples to give an idea.
The 4 slides will be printed with each slide being 3.5 x 5 inches gloss brochure.
We want the front page to have the picture shown or very similar.
The middle of the brochure should look like the center-fold of a passport slide 2 should be the left page of a passport and slide 3 would be the right side of a passport and have an approved symbol
Slide 3 should have an integrated picture of the Marrowby Building
The back should look like the back of a passport and contain our logo, attached.

Hello and Thank you all for your great designs. Can everyone please ensure that all pages(front and back) within each design are added to the same submission. Thanks, Darius

```html
<!DOCTYPE html>
<html lang="en">
<head>
<meta charset="utf-8">
<title>Verlow Consulting – Career Beacon Program Brochure</title>
<link href="https://fonts.googleapis.com/css2?family=Barlow:wght@400;500;600;700&display=swap" rel="stylesheet">
<style>
:root{
  --blue:#1b63b5;
  --band:#1f72bf;
  --soft-blue:#8faad6;
  --ink:#1d1d1d;
  --paper:#ffffff;
  --visa:#f1f0f3;
  --visa-edge:#e4e2e8;
  --maroon:#6e1e33;
  --grey-label:#9a9aa2;
}
*{margin:0;padding:0;box-sizing:border-box}
html,body{width:831px;height:1200px;overflow:hidden;background:#fff}
body{position:relative;font-family:"Barlow",Arial,sans-serif;color:var(--ink)}
.spread{position:absolute;left:58px;width:688px;height:491px;display:flex;box-shadow:6px 8px 10px rgba(0,0,0,.28)}
.spread--outer{top:57px}
.spread--inner{top:595px;border-radius:22px}
.page{position:relative;width:344px;height:100%;overflow:hidden;background:var(--paper)}
.page + .page{border-left:1px solid #bdbdbd}
.spread--inner .page{background:linear-gradient(135deg,#f6f5f8,var(--visa) 60%,var(--visa-edge))}
.spread--inner .page--left{border-radius:22px 0 0 22px}
.spread--inner .page--right{border-radius:0 22px 22px 0}

.url{position:absolute;left:38px;bottom:14px;color:#fff;font-weight:600;font-size:11.5px;letter-spacing:.2px}

/* back cover */
.intro-title{position:absolute;left:38px;top:29px;width:290px;color:var(--blue);font-weight:700;font-size:17.5px;line-height:21px}
.intro-body{position:absolute;left:38px;top:114px;width:270px;font-size:12.3px;line-height:15px}
.objectives{position:absolute;left:38px;top:204px;width:270px;list-style:none;color:var(--blue);font-weight:600;font-size:10.3px;line-height:13.7px}
.objectives li{position:relative;padding-left:18px;margin-bottom:9px}
.objectives li span{position:absolute;left:0}
.photo-passports{position:absolute;left:0;bottom:0;width:272px;height:98px;background:linear-gradient(100deg,#25407c 0%,#8a1f2c 30%,#a8232f 70%,#c9c9cf 100%);border-radius:0 40px 0 0}

/* front cover */
.brand{position:absolute;left:30px;top:26px;display:flex;align-items:center;gap:10px}
.brand-mark{width:34px;height:34px;border-radius:50%;background:var(--blue)}
.brand-name{color:var(--blue);font-weight:700;font-size:14px}
.brand-tag{position:absolute;left:30px;top:82px;color:var(--blue);font-size:10px;line-height:11px}
.cover-band{position:absolute;left:0;top:163px;width:100%;height:66px;background:var(--band);color:#fff;padding:9px 0 0 31px}
.cover-band h1{font-weight:700;font-size:19px;line-height:23px}
.cover-band p{font-size:19px;line-height:23px}
.photo-passport{position:absolute;left:0;top:229px;width:100%;height:262px;background:radial-gradient(ellipse at 30% 20%,#8a2a40,var(--maroon) 55%,#4c1222)}

/* inner pages */
.visas-label{position:absolute;top:40px;color:var(--grey-label);font-weight:600;font-size:10px;letter-spacing:3px}
.page--left .visas-label{left:162px}
.page--right .visas-label{left:144px;top:34px}
.salary-tag{position:absolute;left:0;top:53px;width:145px;height:48px;background:var(--soft-blue);border-radius:0 12px 12px 0;color:#fff;font-weight:600;font-size:13px;line-height:16px;padding:8px 0 0 32px}
.inner-title{position:absolute;color:var(--blue);font-weight:700;font-size:20px;line-height:25px}
.page--left .inner-title{left:32px;top:112px}
.page--right .inner-title{left:39px;top:48px}
.subhead{position:absolute;font-weight:700;font-size:13px}
.page--left .subhead{left:32px;top:160px}
.page--right .subhead{left:39px;top:114px}
.learn{position:absolute;top:185px;list-style:none;font-size:11px;line-height:13.7px}
.learn li{position:relative;padding-left:11px;margin-bottom:5px}
.learn li::before,.overview li::before{content:"";position:absolute;left:0;top:5px;width:4px;height:4px;border-radius:50%;background:currentColor}
.learn--a{left:32px;width:145px}
.learn--b{left:182px;width:130px}
.overview{position:absolute;left:39px;top:144px;width:285px;list-style:none;font-size:11px;line-height:14px}
.overview li{position:relative;padding-left:11px;margin-bottom:7px}
.overview .highlight{color:var(--blue);font-weight:600;margin-bottom:4px}
.overview .gap{margin-top:14px}
.offer{position:absolute;left:38px;top:349px;width:296px;height:131px;background:var(--soft-blue);display:flex}
.offer-text{width:190px;padding:10px 0 0 12px;color:#fff;font-size:11px;line-height:14px}
.offer-text strong{font-weight:600}
.offer-text .loc{margin-top:14px}
.photo-building{flex:1;background:linear-gradient(160deg,#d7e4ef,#7f9fbd 45%,#3e5d7e)}
</style>
</head>
<body>

<section class="spread spread--outer">
  <div class="page page--left back-cover">
    <h2 class="intro-title">Verlow Consulting is a London based firm specialising in Financial Recruitment &amp; Training</h2>
    <p class="intro-body">Our belief is everyone deserves a shot at a career in Finance, for that reason there is no pre-requisites to apply for the program. This program is designed with two main objectives in mind:</p>
    <ol class="objectives">
      <li><span>1.</span>To provide participants with a step by step guide through the world of finance and allow people with no previous experience or knowledge of finance to understand how Banking and the Economy function.</li>
      <li><span>2.</span>To prepare people to work in finance. This course is delivered by ex financial professionals who will teach you how Investment Banks work. We have strong relationships with the top financial instructions and work directly with their hiring Managers to secure permanent employment for attendees.</li>
    </ol>
    <div class="photo-passports" role="img" aria-label="Photo of blue and red passports"></div>
    <p class="url">www.verlowconsulting.com</p>
  </div>
  <div class="page page--right front-cover">
    <div class="brand"><span class="brand-mark"></span><span class="brand-name">Verlow Consulting</span></div>
    <p class="brand-tag">Financial Recruitment<br>with Expertise</p>
    <div class="cover-band">
      <h1>Want to work in Finance?</h1>
      <p>Claim your Passport to the city!</p>
    </div>
    <div class="photo-passport" role="img" aria-label="Close-up photo of a burgundy passport cover"></div>
    <p class="url">www.verlowconsulting.com</p>
  </div>
</section>

<section class="spread spread--inner">
  <div class="page page--left">
    <span class="visas-label">VISAS</span>
    <div class="salary-tag">Average starting<br>salary - £35,000</div>
    <h2 class="inner-title">Lets get you on your way</h2>
    <h3 class="subhead">What you can expect to learn:</h3>
    <ul class="learn learn--a">
      <li>Everything you need to know to work in Finance</li>
      <li>The history of Banking and Finance</li>
      <li>Finance Fundamentals - Macro Economics and the big picture</li>
      <li>Corporate Investment Banking – M&amp;A, IPOs, LBO</li>
      <li>Capital Markets and the various Assets Classes- Fixed Income Equity etc.</li>
      <li>Financial Instruments - Bonds, Stocks etc.</li>
      <li>Derivatives Overview- CDS, CDOs, Futures, Options, Swaps etc.</li>
    </ul>
    <ul class="learn learn--b">
      <li>Financial Players - Banks, Buy Side firms, Brokers etc.</li>
      <li>Markets and Exchanges - How they work, how people make money</li>
      <li>Banking Terminology - All the buss words and financial terms needed</li>
      <li>Business Etiquette - Not taught but extremely important to a successful career</li>
      <li>Fully Financial/Banking Crisis discussion and explanation</li>
    </ul>
  </div>
  <div class="page page--right">
    <span class="visas-label">VISAS</span>
    <h2 class="inner-title">The Verlow Career<br>Beacon Program</h2>
    <h3 class="subhead">Program Overview:</h3>
    <ul class="overview">
      <li>One Day Financial Training Crash Course, delivered by Financial Professionals (Worth £965)</li>
      <li>One to One Interview Training with a Financial Professional (Worth £125)</li>
      <li>CV Review with Experienced Recruitment Consultant (Worth £45)</li>
      <li class="highlight gap">Entry into Work Experience Programme</li>
      <li class="highlight">Individual assistance with the Harbourline Recruitment Consultant</li>
    </ul>
    <div class="offer">
      <div class="offer-text">
        <p><strong>Total Value £1135<br>Voucher Code 20% off<br>CBPMAR15</strong></p>
        <p class="loc"><strong>Location:</strong><br>Applicants will attend training in our offices at Level 30, Marrowby Building</p>
      </div>
      <div class="photo-building" role="img" aria-label="Photo of the Marrowby Building glass tower"></div>
    </div>
  </div>
</section>

</body>
</html>
```